Business card for a new cabinet shop company named Marlowe Cabinets for high end cabinets

Design a business card, thinking dark rich green with colours to speak of high end luxury ie; cream, gold, black possibly

Peter Lindqvar
Director Craftsman
Email: info@marlowecabinets.com.au
Instagram : @marlowe.cabinets

```html
<!DOCTYPE html>
<html lang="en">
<head>
<meta charset="utf-8">
<title>Marlowe Cabinets – Business Card</title>
<link href="https://fonts.googleapis.com/css2?family=Poppins:wght@400;500;600&display=swap" rel="stylesheet">
<style>
  :root {
    --page-bg: #e8e4de;
    --card-light: #f4f3f1;
    --card-mid: #e2e1df;
    --gold: #9a7430;
    --gold-light: #b8914a;
    --black: #151515;
    --ink: #2a2a2a;
    --ink-soft: #4a4a4a;
  }
  html, body {
    margin: 0;
    padding: 0;
    width: 1200px;
    height: 970px;
    overflow: hidden;
    background: var(--page-bg);
    font-family: "Poppins", sans-serif;
  }
  .canvas {
    position: relative;
    width: 1200px;
    height: 970px;
  }
  .business-card {
    position: absolute;
    left: 50px;
    top: 171px;
    width: 1100px;
    height: 628px;
    background: linear-gradient(135deg, var(--card-light) 0%, #ecebe9 50%, var(--card-mid) 100%);
    box-shadow: 0 18px 40px rgba(0,0,0,0.18);
    overflow: hidden;
  }
  .decor-corner {
    position: absolute;
    left: 0;
    top: 0;
    width: 14px;
    height: 100%;
    background: linear-gradient(180deg, var(--gold) 0%, var(--gold-light) 50%, var(--gold) 100%);
  }
  .decor-band {
    position: absolute;
    left: 0;
    bottom: 0;
    width: 100%;
    height: 48px;
    background: linear-gradient(90deg, var(--gold) 0%, var(--gold-light) 45%, #6b5226 75%, var(--black) 100%);
  }
  .brand-block {
    position: absolute;
    right: 66px;
    top: 100px;
    display: flex;
    align-items: center;
    gap: 26px;
  }
  .brand-square {
    width: 96px;
    height: 96px;
    border: 4px solid var(--gold);
    box-sizing: border-box;
  }
  .brand-name {
    margin: 0;
    font-weight: 500;
    font-size: 54px;
    line-height: 1.05;
    color: var(--gold);
    letter-spacing: 1px;
  }
  .person {
    position: absolute;
    left: 57px;
    top: 300px;
    padding-left: 29px;
    border-left: 3px solid var(--gold);
  }
  .person-name {
    margin: 0;
    font-weight: 600;
    font-size: 35px;
    line-height: 1.1;
    color: var(--ink);
  }
  .person-role {
    margin: 0;
    font-weight: 400;
    font-size: 23px;
    line-height: 1.3;
    color: var(--ink-soft);
  }
  .contact-list {
    position: absolute;
    left: 52px;
    top: 413px;
    margin: 0;
    padding: 0;
    list-style: none;
  }
  .contact-item {
    display: flex;
    align-items: center;
    gap: 18px;
    height: 36px;
    font-size: 27px;
    color: var(--ink);
  }
  .contact-icon {
    width: 20px;
    height: 20px;
    flex: none;
  }
</style>
</head>
<body>
<main class="canvas">
  <section class="business-card" aria-label="Marlowe Cabinets business card">
    <div class="decor-corner" role="img" aria-label="Gold accent strip along the card edge"></div>
    <div class="decor-band" role="img" aria-label="Gold and black decorative band along the bottom edge"></div>

    <div class="brand-block">
      <div class="brand-square"></div>
      <p class="brand-name">Marlowe<br>Cabinets</p>
    </div>

    <div class="person">
      <h1 class="person-name">Peter Lindqvar</h1>
      <p class="person-role">Craftsman</p>
    </div>

    <ul class="contact-list">
      <li class="contact-item">
        <svg class="contact-icon" viewBox="0 0 20 20" aria-hidden="true">
          <path d="M5 2 L8 2 L9 6 L7 8 C8 11 9 12 12 13 L14 11 L18 12 L18 15 C18 17 16 18 14 18 C7 17 3 13 2 6 C2 4 3 2 5 2 Z" fill="var(--gold)"/>
        </svg>
        <span>(555) 218-4630</span>
      </li>
      <li class="contact-item">
        <svg class="contact-icon" viewBox="0 0 20 20" aria-hidden="true">
          <rect x="1" y="4" width="18" height="12" fill="var(--gold)"/>
          <path d="M1 4 L10 11 L19 4" fill="none" stroke="#f4f3f1" stroke-width="1.5"/>
        </svg>
        <span>info@marlowecabinets.com.au</span>
      </li>
      <li class="contact-item">
        <svg class="contact-icon" viewBox="0 0 20 20" aria-hidden="true">
          <circle cx="10" cy="10" r="8" fill="var(--gold)"/>
        </svg>
        <span>@marlowe.cabinets</span>
      </li>
    </ul>
  </section>
</main>
</body>
</html>
```